Crowdsourced IT recruitment agency - velmorix

We need an engaging and smart website design for VELMORIX Crowd recruitment. We are young innovative IT recruitment company. We have deep expertise in all IT & digital areas and using crowdsourcing to search the best market candidates faster than ever.
Our mission: to connect people and organizations interests, inspiring each other and enabling together reach better results.

We would like the design to be personalized, emotional, yet simple and neat. It should focus on the person with a problem which we solve.

Reading the site customers should feel safe and confident that velmorix is the trusted partner and everything we do is a quality product.

We also focus on long term relationship with our clients.

We have 4 products:
IT Recruitment – professional recruitment of candidates in IT and digital areas
IT RPO – candidates research process outsourcing(RPO) - provision of resume pools for the client
Kestrel Talent School – training, seminars and networking events for HR professionals from IT and hi-tech companies
Plumview Board – a tool for data visualization in nice and interactive dashboards. It pulls data from different corporate sources (SAP, Oracle, excel, etc.). It looks like a dashboard, on which there are several graphs or diagrams with HR and business KPIs(key performance indicators)

We like material design sites but also open for other options/ideas

Current site velmorix-hire.ru

Examples of websites that we like:
http://www.quobrant.ru
https://dunmirecardio.ru

Site structure:
About us (description, mission, team, clients, office)
Products: Plumview Board, HR IPO, It Recruitment
Kestrel Talent School (list of events (past and future) with the ability to upload photos, descriptions, etc.)
News: Publications, Articles, Blog
Contacts

Industry/Entity Type

Consulting

Number of Pages Required

5+ page

Font styles to use
Serif
Sans Serif

Requirements
Must have
• Individual blocks with the transition to a separate page for each product
• Link to social network (fb, link),
• Subscribe to news on the main page
• Feedback form
• Site structure:
• About us (description, mission, team, clients, office)
• Products: Plumview Board, HR IPO, It Recruitment
• Kestrel Talent School (list of events (past and future) with the ability to upload photos, descriptions, etc.)
• News: Publications, Articles, Blog, Calendars
• Contacts
Should not have
• too crowded
• too complicatied
• without advertising banners
• crammed

```html
<!DOCTYPE html>
<html lang="en">
<head>
<meta charset="utf-8">
<title>VELMORIX Crowd recruitment</title>
<link rel="stylesheet" href="https://fonts.googleapis.com/css2?family=Open+Sans:wght@400;600;700&family=Roboto:wght@700&display=swap">
<style>
  :root {
    --accent: #1f96d4;
    --accent-bright: #2ea3e3;
    --white: #ffffff;
    --text-soft: #eef1f3;
    --cursor: #9aa0a6;
    --office-light: #a7aba6;
    --office-warm: #8f8d80;
    --office-mid: #5d6468;
    --office-dark: #2a2f33;
    --suit-dark: #1f2328;
  }
  html, body {
    margin: 0;
    padding: 0;
    width: 1200px;
    height: 539px;
    overflow: hidden;
  }
  .hero {
    position: relative;
    width: 1200px;
    height: 539px;
    overflow: hidden;
    font-family: "Open Sans", Arial, sans-serif;
    color: var(--white);
  }
  .hero-photo {
    position: absolute;
    inset: 0;
    background:
      radial-gradient(ellipse 260px 320px at 130px 300px, rgba(143,141,128,0.85), transparent 70%),
      radial-gradient(ellipse 300px 200px at 560px 90px, rgba(167,171,166,0.8), transparent 70%),
      radial-gradient(ellipse 200px 260px at 1110px 150px, rgba(150,156,158,0.7), transparent 70%),
      radial-gradient(ellipse 280px 340px at 900px 380px, rgba(31,35,40,0.95), transparent 70%),
      radial-gradient(ellipse 220px 200px at 420px 330px, rgba(42,47,51,0.85), transparent 70%),
      radial-gradient(ellipse 500px 160px at 400px 520px, rgba(120,124,122,0.6), transparent 70%),
      linear-gradient(180deg, var(--office-mid) 0%, #4a5054 55%, var(--office-dark) 100%);
  }
  .hero-shade {
    position: absolute;
    inset: 0;
    background: rgba(18, 22, 26, 0.38);
  }
  .site-header {
    position: absolute;
    top: 0;
    left: 0;
    right: 0;
    height: 86px;
  }
  .brand {
    position: absolute;
    left: 125px;
    top: 11px;
    display: flex;
    align-items: center;
    gap: 18px;
  }
  .brand-dot {
    width: 64px;
    height: 64px;
    border-radius: 50%;
    background: var(--accent);
  }
  .brand-name {
    font-weight: 700;
    font-size: 28px;
    color: var(--accent-bright);
    letter-spacing: -0.5px;
  }
  .main-nav {
    position: absolute;
    top: 34px;
    left: 688px;
    display: flex;
    align-items: center;
    gap: 20px;
    font-size: 13px;
    font-weight: 600;
  }
  .main-nav a {
    color: var(--white);
    text-decoration: none;
  }
  .main-nav a.is-current { color: var(--accent-bright); }
  .search-icon { margin-left: 2px; }
  .hero-content {
    position: absolute;
    top: 184px;
    left: 0;
    right: 0;
    text-align: center;
  }
  .hero-kicker {
    margin: 0;
    font-size: 20px;
    font-weight: 700;
    letter-spacing: 0.3px;
  }
  .hero-rule {
    width: 36px;
    height: 2px;
    background: var(--white);
    margin: 14px auto 0;
  }
  .hero-title {
    margin: 17px 0 0;
    font-family: "Roboto", Arial, sans-serif;
    font-weight: 700;
    font-size: 76px;
    line-height: 84px;
    letter-spacing: 1px;
  }
  .type-cursor {
    display: inline-block;
    width: 5px;
    height: 66px;
    background: var(--cursor);
    margin-left: 6px;
    vertical-align: -8px;
  }
  .hero-lead {
    margin: 14px auto 0;
    width: 670px;
    font-size: 12.5px;
    line-height: 20px;
    color: var(--text-soft);
  }
  .hero-button {
    display: inline-block;
    margin-top: 16px;
    width: 167px;
    height: 40px;
    line-height: 40px;
    background: var(--accent);
    color: var(--white);
    font-size: 18px;
    text-decoration: none;
    border-radius: 2px;
  }
  .scroll-hint {
    position: absolute;
    left: 591px;
    top: 499px;
  }
</style>
</head>
<body>
<section class="hero">
  <div class="hero-photo" role="img" aria-label="Photo of a bright open office: a man in glasses and a dark suit works at a laptop, colleagues talk on the phone and work behind him"></div>
  <div class="hero-shade"></div>

  <header class="site-header">
    <div class="brand">
      <span class="brand-dot"></span>
      <span class="brand-name">velmorix</span>
    </div>
    <nav class="main-nav">
      <a href="#" class="is-current">HOME</a>
      <a href="#">ABOUT US</a>
      <a href="#">SERVICES</a>
      <a href="#">BLOG</a>
      <a href="#">CONTACT US</a>
      <svg class="search-icon" width="16" height="16" viewBox="0 0 16 16" aria-label="Search">
        <circle cx="9.5" cy="6.5" r="5" fill="none" stroke="#fff" stroke-width="1.5"/>
        <line x1="6" y1="10" x2="1.5" y2="14.5" stroke="#fff" stroke-width="1.5"/>
      </svg>
    </nav>
  </header>

  <div class="hero-content">
    <p class="hero-kicker">WELCOME TO</p>
    <div class="hero-rule"></div>
    <h1 class="hero-title">VELMORIX<span class="type-cursor"></span></h1>
    <p class="hero-lead">we believe in challenging the status quo and we believe in thinking differently. The way we do this is by making our products simple to use and easy to understand, with outstanding performance characteristics.</p>
    <a href="#" class="hero-button">EXPLORE MORE</a>
  </div>

  <svg class="scroll-hint" width="18" height="18" viewBox="0 0 18 18" aria-label="Scroll down">
    <circle cx="9" cy="9" r="8" fill="none" stroke="#fff" stroke-width="1.4"/>
    <polyline points="5.5,7.5 9,11 12.5,7.5" fill="none" stroke="#fff" stroke-width="1.4"/>
  </svg>
</section>
</body>
</html>
```